A Leisure SPA Plaza Hotel needs Creative VIP Cards Design

We need VIP Cards Design for a SPA Plaza Hotel, This leisure SPA plaza hotel have multiple sub projects, such as leisure hotel room, large buffet restaurant, swimming pool, theatrical performances, sauna bath, massage, SPA, Tea bar, 3D cinema, KTV rooms, chess room, Internet cafes , art appreciation, children's Castle, Korean geothermal, table tennis, billiard room, GYM and other entertainments.
We need Three creative VIP Card design for 3 different level:
1. Golden Card
2. Platinum Card
3. Diamond Card
Attached, Please find the LOGO file and some sample, we new design with much better look than those samples.

```html
<!DOCTYPE html>
<html lang="en">
<head>
<meta charset="UTF-8">
<title>VIP Membership Cards – Seabreeze Garden Plaza</title>
<link href="https://fonts.googleapis.com/css2?family=Antonio:wght@300;400&family=Noto+Sans+SC:wght@500&display=swap" rel="stylesheet">
<style>
  :root {
    --canvas: #000000;
    --gold: #c3c158;
    --platinum: #85849f;
    --diamond: #8dafe2;
    --ink: #0d0d0d;
    --paper: #ffffff;
  }
  * { margin: 0; padding: 0; box-sizing: border-box; }
  html, body {
    width: 1200px; height: 1200px; overflow: hidden;
    background: var(--canvas);
  }
  .card-stack {
    position: relative; width: 1200px; height: 1200px;
  }
  .vip-card {
    position: absolute; left: 360px;
    width: 480px; height: 275px;
    border-radius: 12px;
    overflow: hidden;
  }
  .vip-card--gold { top: 120px; background: var(--gold); }
  .vip-card--platinum { top: 465px; background: var(--platinum); }
  .vip-card--diamond { top: 810px; background: var(--diamond); }

  .tier-label {
    position: absolute; left: 18px; bottom: 24px;
    writing-mode: vertical-rl;
    transform: rotate(180deg);
    display: flex; align-items: flex-end;
    font-family: "Antonio", "Oswald", sans-serif;
    color: var(--ink);
    line-height: 1;
  }
  .tier-label__vip {
    font-size: 56px; font-weight: 300; letter-spacing: 1px;
  }
  .tier-label__rule {
    width: 2px; height: 0;
    inline-size: 34px;
    block-size: 2px;
    background: var(--ink);
    margin: 10px 0 0 0;
    align-self: flex-start;
  }
  .tier-label__name {
    font-size: 29px; font-weight: 400; letter-spacing: 1px;
    padding-bottom: 2px;
    margin-right: 2px;
  }

  .brand {
    position: absolute; left: 120px; right: 18px; top: 50px;
    display: flex; flex-direction: column; align-items: center;
    color: var(--paper);
    font-family: "Noto Sans SC", sans-serif;
    font-weight: 500;
  }
  .brand__mark {
    width: 112px; height: 112px; border-radius: 50%;
    background: var(--paper);
    margin-bottom: 18px;
  }
  .brand__cn { font-size: 34px; letter-spacing: 2px; line-height: 1.1; }
  .brand__en { font-size: 21px; line-height: 1.4; }
</style>
</head>
<body>
<main class="card-stack">

  <section class="vip-card vip-card--gold">
    <div class="tier-label">
      <span class="tier-label__vip">VIP</span>
      <span class="tier-label__rule"></span>
      <span class="tier-label__name">GOLDEN</span>
    </div>
    <div class="brand">
      <span class="brand__mark"></span>
      <span class="brand__cn">海风花园广场</span>
      <span class="brand__en">Seabreeze Garden Plaza</span>
    </div>
  </section>

  <section class="vip-card vip-card--platinum">
    <div class="tier-label">
      <span class="tier-label__vip">VIP</span>
      <span class="tier-label__rule"></span>
      <span class="tier-label__name">PLATINUM</span>
    </div>
    <div class="brand">
      <span class="brand__mark"></span>
      <span class="brand__cn">海风花园广场</span>
      <span class="brand__en">Seabreeze Garden Plaza</span>
    </div>
  </section>

  <section class="vip-card vip-card--diamond">
    <div class="tier-label">
      <span class="tier-label__vip">VIP</span>
      <span class="tier-label__rule"></span>
      <span class="tier-label__name">DIAMOND</span>
    </div>
    <div class="brand">
      <span class="brand__mark"></span>
      <span class="brand__cn">海风花园广场</span>
      <span class="brand__en">Seabreeze Garden Plaza</span>
    </div>
  </section>

</main>
</body>
</html>
```